UI/ UX Design for ERP Software

We need a new UX/UI interface for a ERP software for property managers. Our CMMS / ERP solution is made based on responsive design technologies and is coded in PHP.
The overall UX to be similar to Tarn Vexa - easy navigation, intuitive menus.

Industry/Entity Type

Property Management

Number of Pages Required

5+ page

Requirements
Must have
• Round dock buttons
Consistent icons across the application
Enough Spacing between buttons/icons/ menu
Consistent Font
Nice to have
• We would like the UX to allow the users to use the application without /minimum training.
Should not have
• we don't want anything that is classic with respect to UX

```html
<!DOCTYPE html>
<html lang="en">
<head>
<meta charset="utf-8">
<title>Dashboard Re-Design</title>
<link rel="stylesheet" href="https://fonts.googleapis.com/css2?family=Poppins:wght@500;600;700;800&family=Nunito+Sans:wght@400;600;700&display=swap">
<style>
:root{
  --page:#fdfdfe;
  --accent:#3b6cf0;
  --ink:#1f2129;
  --text:#2f3340;
  --muted:#8b93a6;
  --frame:#e9e9ec;
  --surface:#f5f6fa;
  --white:#ffffff;
  --sky:#29a8dd;
  --navy:#1479c2;
  --violet:#7474dd;
  --mint:#0acf9c;
  --line:#c9ccd6;
  --hand:#6d717a;
}
*{box-sizing:border-box;margin:0;padding:0}
html,body{width:1200px;height:979px;overflow:hidden;background:var(--page)}
body{position:relative;font-family:"Nunito Sans",sans-serif;color:var(--text)}
.board-title{position:absolute;left:107px;top:33px;font-family:"Poppins",sans-serif;font-weight:800;font-size:37px;letter-spacing:-0.5px;color:var(--accent)}
.device{position:absolute;left:110px;top:97px;width:981px;height:744px;border-radius:24px;background:var(--frame)}
.screen{position:absolute;left:11px;top:11px;width:959px;height:722px;border-radius:14px;background:var(--surface);overflow:hidden}
.topbar{position:absolute;left:0;top:0;width:100%;height:55px;background:var(--white)}
.brand{position:absolute;left:90px;top:15px;display:flex;align-items:center;gap:7px}
.brand-mark{width:22px;height:22px;background:var(--navy);border-radius:4px}
.brand-name{font-family:"Poppins",sans-serif;font-weight:600;font-size:20px;color:var(--navy)}
.search{position:absolute;left:396px;top:15px;width:278px;height:27px;border:1.5px solid #d9dbe2;border-radius:4px;display:flex;align-items:center;padding-left:22px;gap:8px;font-size:10px;font-weight:600;color:#444a58}
.bell{position:absolute;left:711px;top:16px}
.divider{position:absolute;left:763px;top:9px;width:1px;height:38px;background:#dfe1e7}
.user{position:absolute;left:782px;top:15px;display:flex;align-items:center;gap:5px;font-family:"Poppins",sans-serif;font-weight:500;font-size:11px;color:var(--ink)}
.avatar{width:25px;height:25px;border-radius:50%;background:var(--sky);color:var(--white);font-size:9px;font-weight:600;display:flex;align-items:center;justify-content:center}
.stats{position:absolute;top:90px;left:84px;height:95px}
.info-card{position:absolute;left:0;top:0;width:134px;height:95px;background:var(--white);border-radius:3px;overflow:hidden}
.info-head{height:36px;background:var(--sky);color:var(--white);font-family:"Poppins",sans-serif;font-weight:500;font-size:11px;padding:10px 12px}
.info-figs{display:flex;gap:17px;padding:12px 12px 0}
.fig b{display:block;font-family:"Poppins",sans-serif;font-weight:500;font-size:12px;color:var(--ink)}
.fig span{display:block;font-size:9px;color:var(--muted);margin-top:5px}
.area-card{position:absolute;top:0;width:197px;height:95px;background:var(--white);border-radius:5px;padding:16px 18px}
.area-card h3{font-family:"Poppins",sans-serif;font-weight:500;font-size:11.5px;color:var(--text)}
.area-card .value{font-family:"Poppins",sans-serif;font-weight:600;font-size:20px;margin-top:8px;letter-spacing:-0.2px}
.area-card .unit{font-size:9px;color:var(--muted);margin-top:5px}
.area-icon{position:absolute;right:18px;top:28px;width:40px;height:40px;border-radius:50%;display:flex;align-items:center;justify-content:center}
.total .value{color:var(--navy)}
.total .area-icon{background:#e6eefa}
.rented .value{color:var(--mint)}
.rented .area-icon{background:#e2f8f1}
.vacant .value{color:var(--violet)}
.vacant .area-icon{background:#efeafb}
.chart-panel{position:absolute;left:86px;top:218px;width:786px;height:304px;background:var(--white);border-radius:10px;overflow:hidden}
.chart-head{height:31px;background:var(--sky);display:flex;align-items:center;padding-left:12px;gap:13px;color:var(--white);font-family:"Poppins",sans-serif;font-weight:600;font-size:13px}
.range{position:absolute;right:29px;top:6px;height:20px;background:var(--white);border-radius:3px;font-size:9px;font-weight:700;color:var(--ink);display:flex;align-items:center;padding:0 7px;gap:4px}
.chart{position:absolute;left:0;top:31px}
.chart text{font-family:"Nunito Sans",sans-serif;font-size:10px;fill:var(--text)}
.chart .legend{font-size:11px}
.dock{position:absolute;left:85px;top:554px;width:788px;height:100px;background:var(--white);border-radius:14px}
.dock-item{position:absolute;top:20px;width:61px;height:61px;border-radius:8px;background:#f7f8fb;display:flex;flex-direction:column;align-items:center;justify-content:flex-end;padding-bottom:9px;gap:4px;font-family:"Poppins",sans-serif;font-weight:600;font-size:9px;color:var(--sky);white-space:nowrap}
.dock-item svg{width:24px;height:24px}
.dock-item.active{background:var(--navy);color:var(--white)}
.scrollbar{position:absolute;left:84px;top:672px;width:789px;height:14px;background:var(--white);border-radius:5px}
.scroll-thumb{width:316px;height:14px;background:var(--sky);border-radius:5px}
.pointer{position:absolute;left:570px;top:780px}
.hint{position:absolute;left:0;width:1200px;text-align:center;font-family:"Poppins",sans-serif}
.hint-title{top:868px;font-weight:700;font-size:37px;color:var(--ink);letter-spacing:-0.5px}
.hint-sub{top:925px;font-weight:700;font-size:20.5px;color:var(--accent)}
</style>
</head>
<body>
<h1 class="board-title">DASHBOARD RE-DESIGN</h1>

<div class="device">
  <div class="screen">
    <header class="topbar">
      <div class="brand"><span class="brand-mark"></span><span class="brand-name">Keystay</span></div>
      <div class="search">
        <svg width="11" height="11" viewBox="0 0 12 12" fill="none" stroke="#2f3340" stroke-width="1.8"><circle cx="5" cy="5" r="4"/><path d="M8 8l3 3"/></svg>
        Search
      </div>
      <svg class="bell" width="22" height="24" viewBox="0 0 22 24"><path d="M10 3c-4 0-6 3-6 7v5l-3 3h18l-3-3v-5c0-4-2-7-6-7z" fill="var(--sky)"/><circle cx="10" cy="20" r="2.5" fill="var(--sky)"/><circle cx="17" cy="4" r="4" fill="#f2555a"/></svg>
      <div class="divider"></div>
      <div class="user"><span class="avatar">LV</span>Lorna Vey
        <svg width="10" height="7" viewBox="0 0 10 7" fill="none" stroke="#1f2129" stroke-width="1.5"><path d="M1 1l4 4 4-4"/></svg></div>
    </header>

    <section class="stats">
      <div class="info-card">
        <div class="info-head">Information</div>
        <div class="info-figs">
          <div class="fig"><b>61</b><span>Properties</span></div>
          <div class="fig"><b>28</b><span>Tenants</span></div>
        </div>
      </div>
      <div class="area-card total" style="left:156px">
        <h3>Total Properties Area</h3>
        <div class="value">422,000.00</div>
        <div class="unit">sq.ft.</div>
        <div class="area-icon"><svg width="22" height="22" viewBox="0 0 22 22"><circle cx="11" cy="11" r="10" fill="var(--navy)"/><path d="M5 6c3 0 4 2 3 4s-3 2-2 5M13 3c0 3 3 3 4 5s-2 4 0 7" stroke="#e6eefa" stroke-width="2" fill="none"/></svg></div>
      </div>
      <div class="area-card rented" style="left:374px">
        <h3>Rented Area</h3>
        <div class="value">233,500.00</div>
        <div class="unit">sq.ft.</div>
        <div class="area-icon"><svg width="22" height="20" viewBox="0 0 22 20"><path d="M11 1L1 10h3v9h5v-6h4v6h5v-9h3z" fill="var(--mint)"/></svg></div>
      </div>
      <div class="area-card vacant" style="left:593px">
        <h3>Vacancies Area</h3>
        <div class="value">188,500.00</div>
        <div class="unit">sq.ft.</div>
        <div class="area-icon"><svg width="18" height="20" viewBox="0 0 18 20" fill="var(--violet)"><circle cx="9" cy="5" r="4.5"/><path d="M1 19c0-5 3-8 8-8s8 3 8 8z"/></svg></div>
      </div>
    </section>

    <section class="chart-panel">
      <div class="chart-head">
        <svg width="20" height="15" viewBox="0 0 20 15" fill="var(--white)"><path d="M1 0v14h19v-2H3V0z"/><path d="M4 11l3-6 3 3 3-5 4 8z"/></svg>
        12/27/2020 - 01/03/2021
        <div class="range">Last 7 Days <svg width="7" height="5" viewBox="0 0 7 5" fill="none" stroke="#1f2129" stroke-width="1.2"><path d="M1 1l2.5 2.5L6 1"/></svg></div>
      </div>
      <svg class="chart" width="786" height="273" viewBox="0 0 786 273">
        <g stroke="var(--line)" stroke-width="0.8" stroke-dasharray="3 3">
          <path d="M42 17H757"/><path d="M42 82H757"/><path d="M42 146H757"/>
        </g>
        <path d="M42 8V217H757" stroke="#3a3d48" stroke-width="0.8" fill="none"/>
        <g text-anchor="end">
          <text x="31" y="20">0.75</text><text x="31" y="85">0.5</text><text x="31" y="149">0.25</text><text x="31" y="221">0</text>
        </g>
        <g>
          <rect x="56" y="31" width="23" height="186" rx="1" fill="var(--navy)"/>
          <rect x="79" y="101" width="23" height="116" rx="1" fill="var(--violet)"/>
          <rect x="278" y="134" width="23" height="83" rx="1" fill="var(--mint)"/>
          <rect x="390" y="165" width="23" height="52" rx="1" fill="var(--mint)"/>
          <rect x="413" y="112" width="22" height="105" rx="1" fill="var(--violet)"/>
          <rect x="508" y="48" width="23" height="169" rx="1" fill="var(--mint)"/>
          <rect x="712" y="89" width="23" height="128" rx="1" fill="var(--mint)"/>
          <rect x="735" y="89" width="22" height="128" rx="1" fill="var(--violet)"/>
        </g>
        <g text-anchor="middle">
          <text x="79" y="232">27 Dec</text><text x="190" y="232">28 Dec</text><text x="301" y="232">29 Dec</text><text x="412" y="232">30 Dec</text><text x="531" y="232">01 Jan</text><text x="631" y="232">02 Jan</text><text x="734" y="232">03 Jan</text>
        </g>
        <g>
          <rect x="42" y="246" width="17" height="16" rx="2" fill="var(--navy)"/><text class="legend" x="65" y="258">Scheduled Maintenance</text>
          <rect x="194" y="246" width="17" height="16" rx="2" fill="var(--violet)"/><text class="legend" x="217" y="258">Complete Scheduled Maintenance</text>
          <rect x="399" y="246" width="17" height="16" rx="2" fill="var(--mint)"/><text class="legend" x="422" y="258">Future Scheduled Maintenance</text>
        </g>
      </svg>
    </section>

    <nav class="dock">
      <div class="dock-item active" style="left:24px"><svg viewBox="0 0 24 24" fill="currentColor"><rect x="1" y="1" width="9" height="12"/><rect x="13" y="1" width="10" height="7"/><rect x="1" y="16" width="9" height="7"/><rect x="13" y="11" width="10" height="12"/></svg>Dashboard</div>
      <div class="dock-item" style="left:99px"><svg viewBox="0 0 24 24" fill="currentColor"><circle cx="12" cy="7" r="6"/><path d="M2 23c0-6 4-9 10-9s10 3 10 9z"/></svg>Customers</div>
      <div class="dock-item" style="left:175px"><svg viewBox="0 0 24 24" fill="currentColor"><path d="M12 1L1 11h3v12h6v-7h4v7h6V11h3z"/></svg>Properties</div>
      <div class="dock-item" style="left:250px"><svg viewBox="0 0 24 24" fill="currentColor"><circle cx="12" cy="6" r="5"/><path d="M3 23c0-7 3-10 9-10s9 3 9 10z"/></svg>Tenant</div>
      <div class="dock-item" style="left:326px"><svg viewBox="0 0 24 24" fill="currentColor"><path d="M3 2l5 1 1 5-3 2c2 4 4 6 8 8l2-3 5 1 1 5c-11 1-20-8-19-19z"/><rect x="11" y="2" width="12" height="9" rx="1"/></svg>Contacts</div>
      <div class="dock-item" style="left:401px"><svg viewBox="0 0 24 24" fill="currentColor"><circle cx="5" cy="8" r="3"/><circle cx="12" cy="6" r="4"/><path d="M0 18c0-4 2-6 5-6s5 2 5 6z"/><path d="M5 21c0-6 3-9 7-9s5 2 5 3v6z"/><circle cx="19" cy="17" r="4" fill="none" stroke="currentColor" stroke-width="3"/></svg>Contractor</div>
      <div class="dock-item" style="left:477px"><svg viewBox="0 0 24 24" fill="currentColor"><circle cx="5" cy="8" r="3"/><circle cx="19" cy="8" r="3"/><circle cx="12" cy="6" r="4"/><path d="M0 20c0-5 2-8 5-8s5 3 5 8zM14 20c0-5 2-8 5-8s5 3 5 8z"/><path d="M5 22c0-7 3-10 7-10s7 3 7 10z"/></svg>Employees</div>
      <div class="dock-item" style="left:552px"><svg viewBox="0 0 24 24" fill="currentColor"><path d="M4 1h11l6 6v16H4z"/><path d="M8 18c3-2 5-6 4-9s-2 4 0 6 3 1 4 1" stroke="#f7f8fb" stroke-width="1.3" fill="none"/></svg>Compliance</div>
      <div class="dock-item" style="left:628px"><svg viewBox="0 0 24 24" fill="currentColor"><path d="M11 2l8 1 4 5-3 2-3-3-3 1-10 13-3-3 12-11z"/></svg>Maintenance</div>
      <div class="dock-item" style="left:703px"><svg viewBox="0 0 24 24" fill="currentColor"><path d="M10 1h4l1 3 3 1 3-2 3 3-2 3 1 3 3 1v4l-3 1-1 3 2 3-3 3-3-2-3 1-1 3h-4l-1-3-3-1-3 2-3-3 2-3-1-3-3-1v-4l3-1 1-3-2-3 3-3 3 2 3-1z" transform="scale(0.92) translate(1 1)"/><circle cx="12" cy="12" r="4" fill="#f7f8fb"/></svg>Work Orders</div>
    </nav>

    <div class="scrollbar"><div class="scroll-thumb"></div></div>
  </div>
</div>

<svg class="pointer" width="60" height="82" viewBox="0 0 60 82">
  <path d="M10 20a17 17 0 1 1 34 0" fill="none" stroke="var(--hand)" stroke-width="4"/>
  <path d="M20 22a7 7 0 0 1 14 0v19l18 8c3 1 4 4 4 7v20c0 3-2 5-5 5H28c-2 0-4-1-5-3L6 60c-2-2-2-5 1-6 2-1 5 0 7 2l6 5z" fill="var(--hand)"/>
</svg>

<div class="hint hint-title">Slide Right or Left</div>
<div class="hint hint-sub">The Horizontal Scroll Bar To Access All Menu</div>
</body>
</html>
```